Fernwicks needs product labels for deodorant line, and future soap, and lip balm line.

Fernwicks is a new startup that at this time is looking for labels for our deodorant line. There will be future work for our other products given to the winning designer. Our products are all-natural free from petrochemicals, propylene glycol, parabens, aluminum compounds, or synthetic colorants. All our products are also handmade.
We are using a standard size stick to contain the product, on the front cap the label is 2"W x 1"H, on the body front and back the size is 2" W x 2.675" H. We want the front to say "aluminum free", and "all-natural deodorant"
The back needs to include, a UPC, Our mission is to bring you effective, all-natural products using the highest quality ingredients. , Ingredients Cocoa Butter, Shea Butter, Arrowroot Powder, Sodium Bicarbonate, Olive Oil, Water.
We are launching 4 scents.
scent free
Lavander
Tea Tree
Baby Powder
We included a couple pics of product labels we like but are definitely not limited to them. also a picture of the empty container.
Updates
Project Deadline Extended
Reason: Someone completed their design but didn't post it in time and asked me to extend the dead line.
Target Market(s)
Females that are health conscience.
Industry/Entity Type
Cosmetics

```html
<!DOCTYPE html>
<html lang="en">
<head>
<meta charset="utf-8">
<title>Fernwicks Lavander Deodorant Label</title>
<link rel="stylesheet" href="https://fonts.googleapis.com/css2?family=Open+Sans:wght@300;400;600;800&display=swap">
<style>
  :root {
    --bg: #eceded;
    --label-white: #ffffff;
    --purple-deep: #3f1f5c;
    --purple-main: #5b2d82;
    --purple-mid: #7d55a6;
    --purple-soft: #b9a3d3;
    --purple-mist: #e6def0;
    --ink: #2a2a2a;
    --ink-soft: #333333;
  }
  * { margin: 0; padding: 0; box-sizing: border-box; }
  html, body {
    width: 1200px;
    height: 1200px;
    overflow: hidden;
    background: var(--bg);
    font-family: "Open Sans", Arial, sans-serif;
  }
  .canvas {
    position: relative;
    width: 1200px;
    height: 1200px;
  }
  .label {
    position: absolute;
    left: 160px;
    top: 100px;
    width: 880px;
    height: 1000px;
    box-shadow: 0 6px 24px rgba(0, 0, 0, 0.12);
  }
  .label svg { display: block; width: 100%; height: 100%; }
  .label-base { fill: var(--label-white); }
  .top-band { fill: var(--purple-main); }
  .top-band-line { fill: var(--purple-soft); }
  .swoosh-deep { fill: var(--purple-main); }
  .swoosh-soft { fill: var(--purple-mist); }
  .swoosh-mid { fill: var(--purple-mid); opacity: 0.55; }
  .brand-name {
    fill: var(--ink);
    font-family: "Open Sans", Arial, sans-serif;
    font-weight: 800;
    font-size: 78px;
  }
  .brand-tm {
    fill: var(--ink);
    font-family: "Open Sans", Arial, sans-serif;
    font-weight: 400;
    font-size: 22px;
  }
  .badge-ring { fill: var(--purple-soft); }
  .badge-core { fill: var(--purple-main); }
  .badge-text {
    fill: var(--label-white);
    font-family: "Open Sans", Arial, sans-serif;
    font-weight: 400;
    font-size: 27px;
  }
  .scent-name {
    fill: var(--label-white);
    font-family: "Open Sans", Arial, sans-serif;
    font-weight: 400;
    font-size: 50px;
    letter-spacing: 1px;
  }
  .product-type {
    fill: var(--purple-mist);
    font-family: "Open Sans", Arial, sans-serif;
    font-weight: 300;
    font-size: 27px;
  }
  .divider { stroke: var(--purple-soft); stroke-width: 2; }
  .net-weight {
    fill: var(--ink-soft);
    font-family: "Open Sans", Arial, sans-serif;
    font-weight: 400;
    font-size: 34px;
  }
</style>
</head>
<body>
<main class="canvas">
  <section class="label">
    <svg viewBox="0 0 880 1000" xmlns="http://www.w3.org/2000/svg">
      <defs>
        <linearGradient id="dotFieldTone" x1="1" y1="0" x2="0" y2="1">
          <stop offset="0" stop-color="#8e6bb3"/>
          <stop offset="1" stop-color="#ffffff" stop-opacity="0"/>
        </linearGradient>
        <linearGradient id="lavenderPhotoTone" x1="0" y1="0" x2="0.6" y2="1">
          <stop offset="0" stop-color="#d9cce8"/>
          <stop offset="0.35" stop-color="#8a63b2"/>
          <stop offset="0.6" stop-color="#4e2672"/>
          <stop offset="1" stop-color="#3a1a56"/>
        </linearGradient>
        <clipPath id="labelClip">
          <rect width="880" height="1000"/>
        </clipPath>
      </defs>

      <g clip-path="url(#labelClip)">
        <rect class="label-base" width="880" height="1000"/>

        <rect class="top-band" x="0" y="0" width="880" height="28"/>
        <rect class="top-band-line" x="0" y="28" width="880" height="6"/>

        <rect class="dot-field" x="580" y="235" width="300" height="260" fill="url(#dotFieldTone)" role="img" aria-label="Halftone dot texture fading toward the lower left"/>

        <path class="swoosh-soft" d="M0 330 C 260 260, 560 360, 880 330 L 880 560 C 600 520, 300 470, 0 420 Z"/>
        <path class="swoosh-deep" d="M0 360 C 300 320, 560 470, 880 450 L 880 520 C 600 540, 300 430, 0 410 Z"/>
        <path class="swoosh-mid" d="M0 440 C 300 470, 620 560, 880 560 L 880 620 C 600 610, 300 520, 0 470 Z"/>

        <circle class="lavender-photo" cx="250" cy="640" r="330" fill="url(#lavenderPhotoTone)" role="img" aria-label="Close-up photograph of lavender blossoms fading into deep purple"/>

        <g class="brand">
          <text class="brand-name" x="410" y="190" text-anchor="middle">Fernwicks</text>
          <text class="brand-tm" x="622" y="196">TM</text>
        </g>

        <g class="badge">
          <circle class="badge-ring" cx="600" cy="470" r="150"/>
          <circle class="badge-core" cx="600" cy="470" r="138"/>
          <text class="badge-text" x="600" y="430" text-anchor="middle">all skin types</text>
          <text class="badge-text" x="600" y="466" text-anchor="middle">+</text>
          <text class="badge-text" x="600" y="502" text-anchor="middle">aluminum</text>
          <text class="badge-text" x="600" y="536" text-anchor="middle">free</text>
        </g>

        <g class="scent">
          <text class="scent-name" x="70" y="770">LAVANDER</text>
          <text class="scent-name" x="70" y="828">Scent</text>
          <line class="divider" x1="70" y1="850" x2="430" y2="850"/>
          <text class="product-type" x="70" y="888">All-Natural Deodorant</text>
        </g>

        <g class="weight">
          <text class="net-weight" x="755" y="920" text-anchor="middle">NET WT 60g</text>
          <text class="net-weight" x="755" y="962" text-anchor="middle">(12.3 OZ)</text>
        </g>
      </g>
    </svg>
  </section>
</main>
</body>
</html>
```